Business card design incorporating discount offer

We are a trade services company and we need a double sided business card that is going to be used by our tradesmen to give to customers on completion of their jobs.

Below are the key elements of the card that we would like to include:

-Main logo with text 'Corvane Building Aid' underneath.
-Up to 12 smaller icon logos with text 'Your local all-trade experts' to emphasise the point that we cover all the trades
-Discount offer - 10% discount
-Telephone number and website address
-Blank space for tradesman to enter his/her name
-Request for customer feedback with feedback url

This business card will be printed on regular card. In the past we have favoured designs that use a black background but we're open to new ideas.

I have attached a few files:

-A simple wire frame example to show how this card could look with the different elements mentioned above, feel free to use a layout similar to this or come up with something totally different (biz-card.pdf)
-Front and back of a loyalty card the we've used in the past (this card was printed on plastic)
-Front and back of a key fob design that we've previously used (this card was printed on plastic)
-A logo file with the 12 small icons and the main logo image

If you need further images or information please ask.

```html
<!DOCTYPE html>
<html lang="en">
<head>
<meta charset="utf-8">
<title>Corvane Building Aid – Business Card</title>
<link href="https://fonts.googleapis.com/css2?family=Lexend:wght@300;400;600;700&display=swap" rel="stylesheet">
<style>
  :root {
    --page: #e4e4e4;
    --card-white: #ffffff;
    --ink: #111111;
    --brand-blue: #1479c4;
    --muted: #8c8c8c;
    --c-bathrooms: #a23a8f;
    --c-carpentry: #d9a021;
    --c-electric: #9a9a9a;
    --c-handyman: #f2d12a;
    --c-painting: #e23b2b;
    --c-alltrades: #1a78c2;
    --c-building: #b88650;
    --c-drainage: #6b7f8c;
    --c-gas: #1ea3dc;
    --c-kitchen: #2cb5b0;
    --c-pest: #6ab745;
    --c-plumbing: #1c7fc6;
  }
  * { box-sizing: border-box; margin: 0; padding: 0; }
  html, body { width: 1200px; height: 773px; overflow: hidden; }
  body {
    background: var(--page);
    font-family: "Lexend", "Helvetica Neue", Arial, sans-serif;
    position: relative;
  }
  .card {
    position: absolute;
    left: 316px;
    width: 548px;
    height: 329px;
    background: var(--card-white);
    overflow: hidden;
  }
  .card--front { top: 41px; }
  .card--back { top: 389px; }

  /* Front */
  .front-shapes { position: absolute; inset: 0; }
  .brand {
    position: absolute; left: 27px; top: 42px;
    display: flex; align-items: center; gap: 8px;
  }
  .brand__dot { width: 30px; height: 30px; border-radius: 50%; background: var(--brand-blue); }
  .brand__name { font-size: 30px; font-weight: 700; color: var(--ink); letter-spacing: 0.5px; }
  .brand__tagline {
    position: absolute; left: 27px; top: 88px;
    font-size: 14px; font-weight: 600; color: var(--ink);
  }
  .contact { position: absolute; left: 27px; top: 248px; display: flex; gap: 10px; align-items: center; }
  .contact__icon { width: 32px; height: 40px; }
  .contact__phone { font-size: 22px; font-weight: 400; color: var(--ink); line-height: 26px; }
  .contact__web { font-size: 22px; font-weight: 400; color: var(--brand-blue); line-height: 26px; }
  .offer { position: absolute; right: 16px; top: 30px; text-align: right; color: #fff; }
  .offer__value { font-size: 82px; font-weight: 400; line-height: 82px; }
  .offer__title { font-size: 38px; font-weight: 300; line-height: 42px; }
  .offer__sub { font-size: 30px; font-weight: 300; line-height: 34px; }
  .offer__note { font-size: 19px; font-weight: 300; line-height: 23px; margin-top: 24px; }

  /* Back */
  .trades {
    position: absolute; left: 0; top: 0; width: 100%; height: 165px;
    background: var(--ink);
    display: grid; grid-template-columns: repeat(6, 1fr);
    grid-template-rows: 1fr 1fr;
    padding: 26px 6px 6px;
    row-gap: 4px;
  }
  .trade { display: flex; flex-direction: column; align-items: center; gap: 6px; }
  .trade__badge { width: 33px; height: 33px; border-radius: 50%; }
  .trade__label { color: #fff; font-size: 13px; font-weight: 400; white-space: nowrap; }
  .details { position: absolute; right: 20px; top: 180px; text-align: right; color: var(--ink); }
  .details__slogan { font-size: 19px; font-weight: 600; }
  .details__role { font-size: 13px; margin-top: 15px; }
  .details__name { font-size: 17px; font-weight: 700; color: var(--brand-blue); }
  .details__feedback { font-size: 11px; line-height: 13px; margin-top: 25px; }
</style>
</head>
<body>
  <section class="card card--front">
    <svg class="front-shapes" viewBox="0 0 494 296" preserveAspectRatio="none">
      <circle cx="437" cy="145" r="190" fill="var(--brand-blue)"/>
      <circle cx="441" cy="139" r="186" fill="var(--ink)"/>
      <rect x="0" y="288" width="177" height="8" fill="var(--brand-blue)"/>
      <rect x="177" y="288" width="317" height="8" fill="var(--ink)"/>
    </svg>

    <div class="brand">
      <span class="brand__dot"></span>
      <span class="brand__name">Corvane</span>
    </div>
    <p class="brand__tagline">Corvane Building Aid</p>

    <div class="contact">
      <svg class="contact__icon" viewBox="0 0 24 30">
        <path d="M6 4 L10 4 L12 10 L9 12 C10 16 13 19 16 20 L18 17 L23 19 L23 23 C23 25 21 26 19 26 C10 25 3 18 2 9 C2 6 4 4 6 4 Z" fill="var(--muted)"/>
      </svg>
      <div>
        <p class="contact__phone">0800 555 0142</p>
        <p class="contact__web">corvane-aid.co.uk</p>
      </div>
    </div>

    <div class="offer">
      <p class="offer__value">10%</p>
      <p class="offer__title">Discount</p>
      <p class="offer__sub">With This Card</p>
      <p class="offer__note">Check our website for<br>full offer details</p>
    </div>
  </section>

  <section class="card card--back">
    <ul class="trades">
      <li class="trade"><span class="trade__badge" style="background:var(--c-bathrooms)"></span><span class="trade__label">Bathrooms</span></li>
      <li class="trade"><span class="trade__badge" style="background:var(--c-carpentry)"></span><span class="trade__label">Carpentry</span></li>
      <li class="trade"><span class="trade__badge" style="background:var(--c-electric)"></span><span class="trade__label">Electricians</span></li>
      <li class="trade"><span class="trade__badge" style="background:var(--c-handyman)"></span><span class="trade__label">Handyman</span></li>
      <li class="trade"><span class="trade__badge" style="background:var(--c-painting)"></span><span class="trade__label">Painting</span></li>
      <li class="trade"><span class="trade__badge" style="background:var(--c-alltrades)"></span><span class="trade__label">all-trades</span></li>
      <li class="trade"><span class="trade__badge" style="background:var(--c-building)"></span><span class="trade__label">Building</span></li>
      <li class="trade"><span class="trade__badge" style="background:var(--c-drainage)"></span><span class="trade__label">Drainage</span></li>
      <li class="trade"><span class="trade__badge" style="background:var(--c-gas)"></span><span class="trade__label">Gas-heating</span></li>
      <li class="trade"><span class="trade__badge" style="background:var(--c-kitchen)"></span><span class="trade__label">Kitchen</span></li>
      <li class="trade"><span class="trade__badge" style="background:var(--c-pest)"></span><span class="trade__label">Pest-control</span></li>
      <li class="trade"><span class="trade__badge" style="background:var(--c-plumbing)"></span><span class="trade__label">Plumbing</span></li>
    </ul>

    <div class="details">
      <p class="details__slogan">Your local all-trade experts</p>
      <p class="details__role">Your Corvane tradesman:</p>
      <p class="details__name">Tradesman Name</p>
      <p class="details__feedback">What do you think of our service?<br>Please leave feedback online<br>www.corvane-aid.co.uk/feedback</p>
    </div>
  </section>
</body>
</html>
```